VORN - Business cards

Business card to be created for Commercial sales staff

Target Market(s)

Commercial businesses

Industry/Entity Type

Commercial

Contact Information for Business Card

Look professional. For commercial clients

Colors
ffffff

Requirements
Must have
• - Vorn Logo
• - Commercial sales staff as postion
• - room for commerical sales manager role
• - person name and their mobile number
• - Website : vornelectrical.com.au
Nice to have
• White background.
• On back of business card just have the logo no other information
Should not have
• Should only have white background on front of card.

```html
<!DOCTYPE html>
<html lang="en">
<head>
<meta charset="utf-8">
<title>Vorn Business Cards</title>
<link href="https://fonts.googleapis.com/css2?family=Open+Sans:ital,wght@0,400;0,600;0,700;0,800;1,700&display=swap" rel="stylesheet">
<style>
  :root {
    --red: #c42127;
    --ink: #2e2f35;
    --paper: #ffffff;
    --backdrop: #ecebe8;
  }
  * { margin: 0; padding: 0; box-sizing: border-box; }
  html, body { width: 1200px; height: 892px; overflow: hidden; }
  body {
    background: var(--backdrop);
    font-family: "Open Sans", Arial, sans-serif;
    position: relative;
  }
  .card {
    position: absolute;
    left: 300px;
    width: 600px;
    height: 343px;
    background: var(--paper);
    overflow: hidden;
    box-shadow: 0 6px 18px rgba(0,0,0,0.18);
  }
  .card--brand { top: 72px; }
  .card--contact { top: 477px; }
  .card-shapes { position: absolute; inset: 0; width: 100%; height: 100%; }

  .brand-lockup {
    position: absolute;
    left: 100px;
    top: 96px;
    display: flex;
    align-items: center;
    gap: 16px;
  }
  .brand-mark {
    width: 54px; height: 54px;
    border-radius: 50%;
    background: var(--red);
  }
  .brand-name {
    font-weight: 800;
    font-size: 96px;
    line-height: 1;
    letter-spacing: 2px;
    color: var(--ink);
  }
  .brand-web {
    position: absolute;
    left: 112px;
    top: 196px;
    font-weight: 700;
    font-style: italic;
    font-size: 22px;
    color: var(--ink);
    letter-spacing: 0.3px;
  }

  .contact-block {
    position: absolute;
    left: 200px;
    top: 84px;
    color: var(--ink);
  }
  .person-name {
    font-weight: 700;
    font-size: 24px;
    letter-spacing: 0.5px;
    line-height: 1.1;
  }
  .person-role {
    font-weight: 400;
    font-size: 20px;
    line-height: 1.3;
  }
  .divider {
    width: 230px;
    height: 2px;
    background: var(--red);
    margin: 8px 0 16px -20px;
  }
  .contact-line {
    display: flex;
    align-items: center;
    gap: 12px;
    font-size: 17px;
    line-height: 1.7;
  }
  .contact-icon { width: 16px; height: 16px; flex: none; }
</style>
</head>
<body>

  <section class="card card--brand" aria-label="Card back with brand">
    <svg class="card-shapes" viewBox="0 0 600 343" preserveAspectRatio="none">
      <path fill="var(--red)" d="M330,0 L600,0 L600,343 L555,343 Q545,110 330,0 Z"/>
      <path fill="var(--red)" d="M0,70 Q40,280 270,343 L0,343 Z"/>
      <path fill="var(--ink)" d="M60,40 Q200,-5 370,22 Q210,10 60,40 Z"/>
      <path fill="var(--ink)" d="M40,110 Q70,300 530,290 Q300,345 120,300 Q50,240 40,110 Z"/>
    </svg>
    <div class="brand-lockup">
      <span class="brand-mark"></span>
      <span class="brand-name">VORN</span>
    </div>
    <p class="brand-web">www.vornelectrical.com.au</p>
  </section>

  <section class="card card--contact" aria-label="Card front with contact details">
    <svg class="card-shapes" viewBox="0 0 600 343" preserveAspectRatio="none">
      <path fill="var(--red)" d="M0,0 L175,0 Q90,170 175,343 L0,343 Z"/>
      <path fill="var(--red)" d="M600,150 Q565,290 430,343 L600,343 Z"/>
      <path fill="var(--ink)" d="M170,15 Q440,5 600,120 L600,175 Q480,45 170,15 Z"/>
      <path fill="var(--ink)" d="M175,270 Q240,335 340,343 L270,343 Q205,320 175,270 Z"/>
    </svg>
    <div class="contact-block">
      <p class="person-name">FULL NAME</p>
      <p class="person-role">Commercial Sales</p>
      <div class="divider"></div>
      <p class="contact-line">
        <svg class="contact-icon" viewBox="0 0 16 16"><path fill="var(--red)" d="M3.5 1.5l2.5 3-1.5 1.5c.8 1.8 2.2 3.2 4 4l1.5-1.5 3 2.5-1.5 2.5C6.5 13 3 9.5 1.5 3z"/></svg>
        +1 555 018 2736
      </p>
      <p class="contact-line">
        <svg class="contact-icon" viewBox="0 0 16 16"><rect x="1" y="3" width="14" height="10" fill="var(--red)"/><path d="M1.5 3.5L8 9l6.5-5.5" stroke="#fff" stroke-width="1.3" fill="none"/></svg>
        sales@vornmail.net
      </p>
    </div>
  </section>

</body>
</html>
```